依頼概要
カメラで画像認識をし、商品画像をクリップ保存しておけるアプリを開発中で、そのUI・デザイン案の提案をお願い致します。

<<特記>>
・アプリ開発はhttp://www.tasukel.jp/work/detail/31827で進行中です。
・本内容は案レベルです。製品レベルの作り込みは不要です。
・採用された方には、以後のアプリ提供(Kaz/Melvine)に向けたUI・デザインの検討/制作を別途発注(2月着手、3月後半最終納品)したいと思ってます。

<<今回の依頼範囲>> ※添付参照(手書きで恐縮です)
以下4点
(1)カメラ画面
(2)クリップ画面
(3)サービス一覧画面
(4)MyPage画面

<<デザイン方向性>>
・方針:
・シンプル、スッキリ
・ターゲット利用者は広く一般
・アプリ自体は主張しない(プラットフォーム的な位置になり各種媒体と連動するので)

・主な構成色
・白
・グレー(複数諧調可)
・グリーン(複数諧調可、アクセント的に利用、※velo広告の色味に近い)
※https://www.mirusaku.co.jp/search?q=velo+green&hl=ja&tbo=u&tbm=isch&source=univ&sa=X&ei=-kR7TPa2H-5wnBXQp8DzFm&ved=0DF1QsBQ&biw=1377&bih=761
※必要に応じて、他色もご利用ください。

<<各画面の説明>>
<各画面>
(1)カメラ画面
・雑誌など紙面や媒体を撮影すると、商品画像を認識できた場合(2)クリップ画面に遷移します。
・カメラ撮影画面と利用者がわかるよう「ファインダー」的なサポートがあることが望ましいです。
・女性誌のモデル画像などを使っていただけると、利用イメージに近くなります。

(2)クリップ画面
・以下の要素の配置をお願いします。
・商品画像(1で認識できたものだとわかりやすい)
・日付
・媒体名
・商品名
・メモ
・各要素の配置位置は自由にしていただいてOKです。

(3)サービス一覧画面
・以下の要素を1セットとして、一覧配置をお願いします。
・媒体img画像
・媒体名
・媒体紹介文
・各要素の配置位置は自由にしていただいてOKです。
・添付例ではimgはサムネイル的ですが、こだわりません。例えば、画面幅に合わせた画像で、媒体名・紹介文などは画像に重ねるのもアリです。
・添付例では各媒体間に余白がありますが、こだわりません。

(4)MyPage画面
・以下の要素の配置をお願いします。
・商品画像(1で認識できたものもあると、わかりやすい)
・日付
・媒体名
・商品名
・メモ
・各要素の配置位置は自由にしていただいてOKです。
・添付例では各商品間に余白がありますが、こだわりません。

<各画面共通>
・トップバー
・「戻る」ボタンもある
・下部タブバー
・要素: カメラ撮影/サービス一覧/MyPage/設定
・アイコン表現もOKです。
※添付例では、いずれも画面中央と明確に区分けされてますが、グラデーション表現や画面中央部の背景色と同色にするなどもアリです。

<<提出様式>>
・ppt or keynote(各画面1枚、計4ページ)
・各デザインの説明を記載お願いします。
デザイン案の手書きイメージを添付漏れていたようなので、追加します。
当方Tasukelコンペ初めて利用致します。

時間・金額も小さい案件だと思いますので、お手数おかけします。

もし質問・要望ありましたら、ご連絡ください!!

全体として最もスッキリとした印象になっているのが、気に入ったポイントです!スタイリッシュでありながら、主張が強くないところが、今回の案件に合っているかと思います。

短い期間の中でご提案していただき、大変ありがとうございました!

コンペ自体を初めて利用させていただきましたが、皆様の提案いずれも参考になります!

また今後も機会ありましたら、よろしくお願い致します。

```html
<!DOCTYPE html>
<html lang="ja">
<head>
<meta charset="utf-8">
<title>クリップアプリ UI案</title>
<link href="https://fonts.googleapis.com/css2?family=Noto+Sans+JP:wght@400;700&display=swap" rel="stylesheet">
<style>
:root{
  --page:#ffffff;
  --label:#555555;
  --status:#111111;
  --bar-top:#f4f4f4;
  --bar-bottom:#dcdcdc;
  --bar-line:#b9b9b9;
  --green:#6cc03a;
  --green-dark:#4e9a22;
  --body:#ececec;
  --card:#ffffff;
  --text:#333333;
  --muted:#888888;
  --tab:#3a3a3a;
  --tab-dark:#262626;
  --tab-icon:#a8a8a8;
}
*{box-sizing:border-box;margin:0;padding:0}
html,body{width:747px;height:1200px;overflow:hidden;background:var(--page)}
body{position:relative;font-family:"Noto Sans JP",sans-serif;color:var(--text)}
.screen-label{position:absolute;width:219px;text-align:center;font-size:11px;color:var(--label);letter-spacing:.05em}
.screen{position:absolute;width:219px;height:329px;background:var(--body);overflow:hidden;display:flex;flex-direction:column;box-shadow:0 0 0 1px #d0d0d0}
.status-bar{height:9px;background:var(--status);color:#fff;font-size:6px;line-height:9px;text-align:center;flex:none}
.top-bar{height:20px;flex:none;position:relative;background:linear-gradient(var(--bar-top),var(--bar-bottom));border-bottom:1px solid var(--bar-line);font-size:7px;line-height:19px;text-align:center;color:#555}
.back-button{position:absolute;left:4px;top:4px;height:11px;padding:0 5px;border-radius:3px;background:var(--green);color:#fff;font-size:6px;line-height:11px;font-weight:700}
.content{flex:1;position:relative;overflow:hidden}
.tab-bar{height:24px;flex:none;display:flex;background:linear-gradient(var(--tab),var(--tab-dark))}
.tab{flex:1;display:flex;flex-direction:column;align-items:center;justify-content:center;color:var(--tab-icon);font-size:4.5px;gap:1px}
.tab svg{width:10px;height:9px;fill:var(--tab-icon)}
.tab.is-active{background:linear-gradient(#7fd04a,var(--green-dark));color:#fff}
.tab.is-active svg{fill:#fff}

.camera-view{position:absolute;inset:0;background:linear-gradient(#f3f1ee,#e2dfdb)}
.model-photo{position:absolute;left:50px;top:10px;width:120px;height:266px;background:linear-gradient(#6c6c70 0%,#85858a 40%,#5a5a60 100%);border-radius:40px 40px 6px 6px;opacity:.85}
.finder{position:absolute;left:70px;top:96px;width:80px;height:80px;border:1px solid rgba(255,255,255,.9)}

.clip-content{padding:8px}
.clip-photo{height:128px;margin:0 auto;width:150px;background:linear-gradient(#efefef,#dcdcdc);display:flex;align-items:center;justify-content:center;border:1px solid #d6d6d6}
.clip-photo div{width:96px;height:110px;background:linear-gradient(#6a6a6e,#505055);border-radius:14px 14px 4px 4px}
.clip-meta{margin-top:6px;font-size:5px;color:var(--muted);display:flex;justify-content:space-between}
.clip-card{margin-top:4px;background:var(--card);border:1px solid #d8d8d8;border-radius:3px;padding:5px}
.clip-name{display:flex;justify-content:space-between;font-size:6px;font-weight:700}
.clip-name .price{color:var(--green)}
.clip-memo{margin-top:4px;background:var(--card);border:1px solid #d8d8d8;border-radius:3px;padding:5px;font-size:5px;line-height:1.5;color:var(--muted);height:44px}

.list{padding:6px;display:flex;flex-direction:column;gap:5px}
.list-item{background:var(--card);border:1px solid #d6d6d6;border-radius:3px;padding:4px;display:flex;gap:5px;align-items:center;height:59px}
.thumb{width:38px;height:50px;flex:none}
.item-text{flex:1;font-size:5px;line-height:1.5;color:var(--muted)}
.item-title{font-size:6px;font-weight:700;color:var(--text)}
.item-name{font-size:5.5px;font-weight:700;color:var(--text)}
.arrow{width:11px;height:11px;flex:none}
</style>
</head>
<body>

<p class="screen-label" style="left:87px;top:26px">カメラ撮影画面</p>
<p class="screen-label" style="left:443px;top:26px">クリップ画面</p>
<p class="screen-label" style="left:87px;top:592px">サービス一覧画面</p>
<p class="screen-label" style="left:443px;top:592px">MyPage画面</p>

<svg width="0" height="0" style="position:absolute">
  <defs>
    <symbol id="icon-camera" viewBox="0 0 10 9"><path d="M1 2h2l1-1h2l1 1h2v6H1z"/><circle cx="5" cy="5" r="1.6" fill="#555"/></symbol>
    <symbol id="icon-list" viewBox="0 0 10 9"><rect x="1" y="1" width="3" height="3"/><rect x="6" y="1" width="3" height="3"/><rect x="1" y="5" width="3" height="3"/><rect x="6" y="5" width="3" height="3"/></symbol>
    <symbol id="icon-person" viewBox="0 0 10 9"><circle cx="5" cy="2.5" r="2"/><path d="M1 9c0-3 2-4 4-4s4 1 4 4z"/></symbol>
    <symbol id="icon-gear" viewBox="0 0 10 9"><circle cx="5" cy="4.5" r="3.4"/><circle cx="5" cy="4.5" r="1.3" fill="#333"/></symbol>
    <symbol id="icon-arrow" viewBox="0 0 11 11"><circle cx="5.5" cy="5.5" r="5.5" fill="#6cc03a"/><path d="M4.3 3l2.6 2.5-2.6 2.5" stroke="#fff" stroke-width="1.4" fill="none"/></symbol>
  </defs>
</svg>

<!-- Camera screen -->
<section class="screen" style="left:87px;top:155px">
  <div class="status-bar">00:00</div>
  <header class="top-bar">カメラ撮影画面</header>
  <div class="content">
    <div class="camera-view">
      <div class="model-photo" role="img" aria-label="雑誌モデルの撮影写真(グレーのカーディガン)"></div>
      <div class="finder"></div>
    </div>
  </div>
  <nav class="tab-bar">
    <div class="tab is-active"><svg><use href="#icon-camera"/></svg>カメラ撮影</div>
    <div class="tab"><svg><use href="#icon-list"/></svg>サービス一覧</div>
    <div class="tab"><svg><use href="#icon-person"/></svg>MyPage</div>
    <div class="tab"><svg><use href="#icon-gear"/></svg>設定</div>
  </nav>
</section>

<!-- Clip screen -->
<section class="screen" style="left:443px;top:155px">
  <div class="status-bar">00:00</div>
  <header class="top-bar"><span class="back-button">戻る</span>クリップ画面</header>
  <div class="content clip-content">
    <div class="clip-photo"><div role="img" aria-label="認識された商品写真(グレーのカーディガン)"></div></div>
    <div class="clip-meta"><span>2013.01.20</span><span>雑誌名XXX 1月号</span></div>
    <div class="clip-card">
      <div class="clip-name"><span>グレーカーディガン</span><span class="price">¥12,800(税込)</span></div>
    </div>
    <div class="clip-memo">メモ:柔らかな素材で着回しやすいカーディガン。春先まで活躍する一枚です。</div>
  </div>
  <nav class="tab-bar">
    <div class="tab is-active"><svg><use href="#icon-camera"/></svg>カメラ撮影</div>
    <div class="tab"><svg><use href="#icon-list"/></svg>サービス一覧</div>
    <div class="tab"><svg><use href="#icon-person"/></svg>MyPage</div>
    <div class="tab"><svg><use href="#icon-gear"/></svg>設定</div>
  </nav>
</section>

<!-- Service list screen -->
<section class="screen" style="left:87px;top:720px">
  <div class="status-bar">00:00</div>
  <header class="top-bar"><span class="back-button">戻る</span>サービス一覧</header>
  <div class="content list">
    <article class="list-item">
      <div class="thumb" role="img" aria-label="雑誌の表紙画像" style="background:linear-gradient(#e9d6c8,#c98f7a)"></div>
      <div class="item-text"><p class="item-title">雑誌名XXX 1月号</p><p>大人の女性に向けた最新ファッション情報をお届けします。</p></div>
      <svg class="arrow"><use href="#icon-arrow"/></svg>
    </article>
    <article class="list-item">
      <div class="thumb" role="img" aria-label="雑誌の表紙画像" style="background:linear-gradient(#f0e6d8,#b7a28c)"></div>
      <div class="item-text"><p class="item-title">雑誌名XXX 1月号</p><p>毎日のコーディネートに役立つアイテムを紹介します。</p></div>
      <svg class="arrow"><use href="#icon-arrow"/></svg>
    </article>
    <article class="list-item">
      <div class="thumb" role="img" aria-label="雑誌の表紙画像" style="background:linear-gradient(#f2d9d6,#c2414a)"></div>
      <div class="item-text"><p class="item-title">雑誌名XXX 1月号</p><p>話題のブランドと着こなしを特集しています。</p></div>
      <svg class="arrow"><use href="#icon-arrow"/></svg>
    </article>
  </div>
  <nav class="tab-bar">
    <div class="tab"><svg><use href="#icon-camera"/></svg>カメラ撮影</div>
    <div class="tab is-active"><svg><use href="#icon-list"/></svg>サービス一覧</div>
    <div class="tab"><svg><use href="#icon-person"/></svg>MyPage</div>
    <div class="tab"><svg><use href="#icon-gear"/></svg>設定</div>
  </nav>
</section>

<!-- MyPage screen -->
<section class="screen" style="left:443px;top:720px">
  <div class="status-bar">00:00</div>
  <header class="top-bar"><span class="back-button">戻る</span>My Page</header>
  <div class="content list">
    <article class="list-item">
      <div class="thumb" role="img" aria-label="商品写真(グレーのカーディガン)" style="background:linear-gradient(#6d6d72,#4f4f55)"></div>
      <div class="item-text"><p>雑誌名XXX 1月号</p><p class="item-name">グレーカーディガン</p><p>2013.01.20 着回し用メモ</p></div>
      <svg class="arrow"><use href="#icon-arrow"/></svg>
    </article>
    <article class="list-item">
      <div class="thumb" role="img" aria-label="商品写真(ブラウンのスカート)" style="background:linear-gradient(#6a5348,#3f2f29)"></div>
      <div class="item-text"><p>雑誌名XXX 1月号</p><p class="item-name">ブラウンスカート</p><p>2013.01.18 春用メモ</p></div>
      <svg class="arrow"><use href="#icon-arrow"/></svg>
    </article>
    <article class="list-item">
      <div class="thumb" role="img" aria-label="商品写真(ボルドーのニット)" style="background:linear-gradient(#a3354a,#6e1f30)"></div>
      <div class="item-text"><p>雑誌名XXX 1月号</p><p class="item-name">チェック柄ニット</p><p>2013.01.15 購入検討メモ</p></div>
      <svg class="arrow"><use href="#icon-arrow"/></svg>
    </article>
  </div>
  <nav class="tab-bar">
    <div class="tab"><svg><use href="#icon-camera"/></svg>カメラ撮影</div>
    <div class="tab"><svg><use href="#icon-list"/></svg>サービス一覧</div>
    <div class="tab is-active"><svg><use href="#icon-person"/></svg>MyPage</div>
    <div class="tab"><svg><use href="#icon-gear"/></svg>設定</div>
  </nav>
</section>

</body>
</html>
```